Drywall plastering business card design

Attached is my new logo and a picture of my current business card. I would like my new logo incorporated in to the business card and also my website which is:
www.ridgecrestwallfinishers.co.nz
Industry/Entity Type
Business
Contact Information for Business Card
I would like a picture of my van and my new logo on my new business card. See attached files for pictures of my old business card, van picture and logo.
Colors
0555a3
ffffff
Requirements
Must have
- New logo, Van, contact info

```html
<!DOCTYPE html>
<html lang="en">
<head>
<meta charset="utf-8">
<title>Ridgecrest Wall Finishers – Business Card</title>
<link rel="stylesheet" href="https://fonts.googleapis.com/css2?family=Lato:wght@400;700;900&display=swap">
<style>
  :root {
    --brand-blue: #0555a3;
    --deep-blue: #033f86;
    --white: #ffffff;
    --ink: #111111;
    --backdrop: #e9e7e3;
    --sky-top: #6fa6dc;
    --sky-low: #bcd3e6;
    --hills: #6f7d5a;
  }
  * { box-sizing: border-box; margin: 0; padding: 0; }
  html, body {
    width: 1200px; height: 900px; overflow: hidden;
    background: var(--backdrop);
    font-family: "Lato", Arial, sans-serif;
  }
  .business-card {
    position: absolute; left: 75px; top: 150px;
    width: 1050px; height: 600px;
    background: var(--white);
    overflow: hidden;
    box-shadow: 0 14px 34px rgba(0,0,0,.22);
  }
  .card-shapes { position: absolute; inset: 0; }
  .brand {
    position: absolute; left: 95px; top: 330px;
    display: flex; align-items: center; gap: 18px;
  }
  .brand-mark { width: 30px; height: 30px; background: var(--brand-blue); }
  .brand-name {
    font-weight: 900; font-size: 40px; line-height: 1.02;
    color: var(--brand-blue); text-transform: uppercase;
  }
  .contact {
    position: absolute; right: 70px; top: 262px;
    text-align: right; color: var(--ink);
  }
  .contact-name {
    font-weight: 900; font-size: 30px; color: var(--brand-blue);
    letter-spacing: .5px;
  }
  .contact-role { font-weight: 700; font-size: 24px; margin-bottom: 22px; }
  .contact-line {
    display: flex; justify-content: flex-end; align-items: center; gap: 12px;
    font-weight: 700; font-size: 21px; margin-bottom: 10px;
  }
  .contact-line svg { width: 20px; height: 20px; fill: var(--brand-blue); }
  .tagline {
    position: absolute; left: 320px; top: 470px;
    font-weight: 700; font-size: 25px; color: var(--brand-blue);
  }
</style>
</head>
<body>
  <div class="business-card">
    <svg class="card-shapes" viewBox="0 0 1050 600" width="1050" height="600">
      <defs>
        <linearGradient id="scene-tone" x1="0" y1="0" x2="0" y2="1">
          <stop offset="0" stop-color="var(--sky-top)"/>
          <stop offset=".55" stop-color="var(--sky-low)"/>
          <stop offset="1" stop-color="var(--hills)"/>
        </linearGradient>
      </defs>
      <path d="M0 260 C330 255 680 200 1050 130 L1050 175 C700 230 350 270 0 262 Z" fill="var(--brand-blue)"/>
      <path d="M0 0 H1050 V130 C680 200 330 255 0 260 Z" fill="url(#scene-tone)" role="img" aria-label="Photo of the company van parked above a lakeside town with mountains behind"/>
      <path d="M0 548 C180 545 380 565 540 600 L0 600 Z" fill="var(--brand-blue)"/>
      <path d="M1050 340 C1030 450 990 540 890 600 L1050 600 Z" fill="var(--brand-blue)"/>
    </svg>

    <div class="brand">
      <span class="brand-mark"></span>
      <span class="brand-name">Ridgecrest<br>Wall Finishers</span>
    </div>

    <div class="contact">
      <div class="contact-name">MARK HOLLIS</div>
      <div class="contact-role">Proprietor</div>
      <div class="contact-line">027 555 01 42
        <svg viewBox="0 0 24 24"><path d="M6.6 10.8a15 15 0 0 0 6.6 6.6l2.2-2.2a1 1 0 0 1 1-.25 11.4 11.4 0 0 0 3.6.57 1 1 0 0 1 1 1V20a1 1 0 0 1-1 1A17 17 0 0 1 3 4a1 1 0 0 1 1-1h3.5a1 1 0 0 1 1 1 11.4 11.4 0 0 0 .57 3.6 1 1 0 0 1-.25 1z"/></svg>
      </div>
      <div class="contact-line">hello@ridgecrestwallfinishers.co.nz
        <svg viewBox="0 0 24 24"><path d="M2 5h20v14H2z M2 5l10 8 10-8" fill="var(--brand-blue)" stroke="var(--white)" stroke-width="1.5"/></svg>
      </div>
      <div class="contact-line">www.ridgecrestwallfinishers.co.nz
        <svg viewBox="0 0 24 24"><circle cx="10" cy="10" r="6" fill="none" stroke="var(--brand-blue)" stroke-width="3"/><path d="M14.5 14.5l6 6" stroke="var(--brand-blue)" stroke-width="3"/></svg>
      </div>
    </div>

    <div class="tagline">Large Jobs or Small - Always Quality Assured</div>
  </div>
</body>
</html>
```